Store Fixture business needs a buisness card design

We are looking for a business card design for a store fixture company. "KL Shelf Outfitters" we help small businesses with their start up by providing fixtures required to display their products.
It should have a simple yet innovative design in the front, and a refined look to our company.
We would like our logo, to have one of our products "display cases, clothing rack, mannequins" integrated in the design. And the rest of it just a clean look, which gives our address, store hours, and contact number, etc.
The color scheme as seen in the samples can be changed as long as the goal is achieved.
Industry/Entity Type
Business
Contact Information for Business Card
KL Shelf Outfitters
4362 Marlow Ave.
San Antonio,TX 78299
www.klshelfoutfitters.example
klpo@klshelfoutfitter.example
(210) 555-0188
M-F: 9-6pm
Sat: 10-3pm

```html
<!DOCTYPE html>
<html lang="en">
<head>
<meta charset="utf-8">
<title>KL Shelf Outfitters – Business Card</title>
<link rel="stylesheet" href="https://fonts.googleapis.com/css2?family=Exo+2:wght@600;700&family=Open+Sans:wght@400;600&display=swap">
<style>
  :root {
    --backdrop: #e9e4dc;
    --paper: #ffffff;
    --gold: #e0961c;
    --gold-deep: #b8730f;
    --amber-light: #f0a32a;
    --amber-dark: #5a3005;
    --ink: #4a4a4a;
    --ink-soft: #6b6b6b;
    --tile: #ffffff;
  }
  * { box-sizing: border-box; margin: 0; padding: 0; }
  html, body { width: 1200px; height: 950px; overflow: hidden; }
  body {
    background: var(--backdrop);
    font-family: "Open Sans", Arial, sans-serif;
    position: relative;
  }
  .card {
    position: absolute;
    top: 107px;
    width: 420px;
    height: 735px;
    border-radius: 6px;
    box-shadow: 0 10px 30px rgba(0,0,0,.18);
    overflow: hidden;
  }
  /* Front */
  .card-front { left: 150px; background: var(--paper); }
  .card-front .frame {
    position: absolute; inset: 22px;
    border: 2px solid var(--gold);
  }
  .brand {
    position: absolute; top: 96px; left: 0; right: 0;
    display: flex; align-items: center; justify-content: center; gap: 14px;
  }
  .brand-mark { width: 34px; height: 34px; background: var(--gold); }
  .brand-name {
    font-family: "Exo 2", Arial, sans-serif; font-weight: 700;
    font-size: 30px; color: var(--ink); letter-spacing: .5px;
  }
  .contact {
    position: absolute; top: 222px; left: 0; right: 0;
    text-align: center; color: var(--ink-soft);
  }
  .icon { display: block; margin: 0 auto 6px; width: 18px; height: 18px; fill: var(--gold); }
  .person-name {
    font-family: "Exo 2", Arial, sans-serif; font-weight: 700;
    font-size: 27px; color: var(--gold); letter-spacing: 1px; text-transform: uppercase;
  }
  .person-title { font-size: 18px; color: var(--ink); margin-bottom: 26px; }
  .contact-line { font-size: 18px; line-height: 1.45; }
  .contact-group { margin-bottom: 22px; }
  /* Back */
  .card-back {
    left: 630px;
    background: radial-gradient(ellipse at 55% 40%, var(--amber-light) 0%, var(--gold-deep) 55%, var(--amber-dark) 100%);
  }
  .card-back .frame {
    position: absolute; inset: 22px;
    border: 1.5px solid rgba(255,255,255,.75);
  }
  .product { position: absolute; text-align: center; color: #fff; font-size: 18px; }
  .product-tile {
    width: 180px; height: 140px; background: var(--tile);
    border-radius: 18px; padding: 10px; margin-bottom: 6px;
  }
  .product-photo { width: 100%; height: 100%; border-radius: 12px; }
  .photo-rack { background: linear-gradient(160deg, #f4f4f4, #cfcfcf); }
  .photo-case { background: linear-gradient(160deg, #f5f1ef, #b82a1c 60%, #8c1a12); }
  .photo-mannequin { background: radial-gradient(ellipse at 50% 40%, #8a8a8a, #3b3b3b 75%); }
  .product-rack { top: 70px; left: 30px; }
  .product-case { top: 70px; left: 210px; }
  .product-mannequin { top: 300px; left: 120px; }
  .social {
    position: absolute; top: 560px; left: 50px; right: 50px;
    display: flex; align-items: center; gap: 10px;
  }
  .social .rule { flex: 1; height: 1.5px; background: rgba(255,255,255,.8); }
  .social .dot { width: 24px; height: 24px; border-radius: 50%; background: #fff; }
  .hours {
    position: absolute; top: 600px; left: 0; right: 0;
    text-align: center; color: #fff; font-size: 20px;
  }
</style>
</head>
<body>
  <section class="card card-front">
    <div class="frame"></div>
    <div class="brand">
      <span class="brand-mark"></span>
      <span class="brand-name">KL Shelf Outfitters</span>
    </div>
    <div class="contact">
      <svg class="icon" viewBox="0 0 20 20" aria-hidden="true"><circle cx="10" cy="6" r="4.5"/><path d="M2 19c0-5 3.5-7.5 8-7.5s8 2.5 8 7.5z"/></svg>
      <p class="person-name">Dana Whitfield</p>
      <p class="person-title">CEO/Founder</p>
      <div class="contact-group">
        <svg class="icon" viewBox="0 0 20 20" aria-hidden="true"><path d="M10 1a6.5 6.5 0 0 0-6.5 6.5C3.5 12.5 10 19 10 19s6.5-6.5 6.5-11.5A6.5 6.5 0 0 0 10 1zm0 9a2.5 2.5 0 1 1 0-5 2.5 2.5 0 0 1 0 5z"/></svg>
        <p class="contact-line">4362 Marlow Ave.</p>
        <p class="contact-line">San Antonio,TX 78299</p>
      </div>
      <div class="contact-group">
        <p class="contact-line">(210) 555-0188</p>
        <svg class="icon" viewBox="0 0 20 20" aria-hidden="true"><path d="M5 2l3 4-2 2c1 2.5 3.5 5 6 6l2-2 4 3-2 3C9 18 2 11 2 4z"/></svg>
      </div>
      <div class="contact-group">
        <p class="contact-line">klpo@klshelfoutfitter.example</p>
        <svg class="icon" viewBox="0 0 20 20" aria-hidden="true"><path d="M2 4h16v12H2z"/><path d="M2 4l8 7 8-7" fill="none" stroke="#fff" stroke-width="1.5"/></svg>
      </div>
      <div class="contact-group">
        <svg class="icon" viewBox="0 0 20 20" aria-hidden="true"><circle cx="10" cy="10" r="8"/><path d="M2 10h16M10 2c3 3 3 13 0 16M10 2c-3 3-3 13 0 16" fill="none" stroke="#fff" stroke-width="1.2"/></svg>
        <p class="contact-line">www.klshelfoutfitters.example</p>
      </div>
    </div>
  </section>

  <section class="card card-back">
    <div class="frame"></div>
    <figure class="product product-rack">
      <div class="product-tile"><div class="product-photo photo-rack" role="img" aria-label="Photo of a chrome clothing rack"></div></div>
      <figcaption>clothing rack</figcaption>
    </figure>
    <figure class="product product-case">
      <div class="product-tile"><div class="product-photo photo-case" role="img" aria-label="Photo of a glass display case"></div></div>
      <figcaption>display cases</figcaption>
    </figure>
    <figure class="product product-mannequin">
      <div class="product-tile"><div class="product-photo photo-mannequin" role="img" aria-label="Photo of a store mannequin"></div></div>
      <figcaption>mannequins</figcaption>
    </figure>
    <div class="social" aria-hidden="true">
      <span class="rule"></span><span class="dot"></span><span class="dot"></span><span class="dot"></span><span class="rule"></span>
    </div>
    <p class="hours">Mon-Fri: 9-6pm &nbsp;|&nbsp; Sat: 10-3pm</p>
  </section>
</body>
</html>
```